Rivolex.com Trucking Company Website

Need a website designed (no content) for a trucking company, specializing in trucking of ocean containers (intermodal Trucking). Heavy emphasis on technology, using latest technology, providing unabated visibility and realtime information.
clean minimalist industrial website
example:
https://www.bramtiq.com/

Target Market(s)

Professional Business Consumer corporate and small business

Industry/Entity Type

Trucking Company

Number of Pages Required

5+ page

Requirements
Must have
• Industrial Design, simple informative, for a busy professional to view and get the necessary information with out the distractions.
• Blog Page
• Client Log-In on the front page
• Technology page - showing our intensive investments in technology
Nice to have
• If ANY images included, MUST be USA related. Example if include an image of a truck, ensure its a USA model. Do the research.
• included our business card for sample of Logo
• Doesnt not have to be the same color schemes.
Should not have
• moving images

```html
<!DOCTYPE html>
<html lang="en">
<head>
<meta charset="utf-8">
<title>Rivolex.com – Heavy Logistics &amp; Transportation</title>
<link href="https://fonts.googleapis.com/css2?family=Lato:wght@400;700;900&family=Open+Sans:wght@400;600;700&family=Dosis:wght@500;600&display=swap" rel="stylesheet">
<style>
:root{
  --blue:#1d5fa3;
  --blue-bright:#2a66b0;
  --navy:#0c2f5e;
  --ink:#222a33;
  --text:#555b62;
  --card:#262729;
  --card-alt:#3a3b3d;
  --dark:#2a2c2e;
  --footer:#1f2022;
  --white:#ffffff;
  --rule:#4a5560;
}
*{margin:0;padding:0;box-sizing:border-box}
html,body{width:1200px;height:2853px;overflow:hidden;background:var(--white)}
body{position:relative;font-family:"Open Sans",Arial,sans-serif;color:var(--text)}

/* header */
.site-header{position:absolute;left:0;top:0;width:1200px;height:105px;background:var(--white)}
.brand{position:absolute;left:91px;top:26px;font-family:"Lato",sans-serif;font-weight:900;font-size:44px;letter-spacing:3px;color:var(--blue);line-height:1}
.login{position:absolute;left:1012px;top:20px;display:flex;align-items:center;gap:10px;font-family:"Lato",sans-serif;font-weight:700;font-size:15px;letter-spacing:1px;color:var(--blue)}
.nav{position:absolute;top:63px;left:0;width:1200px;font-family:"Lato",sans-serif;font-weight:700;font-size:16px;letter-spacing:1.2px;color:var(--ink)}
.nav span{position:absolute}
.nav .active{color:var(--blue)}

/* hero */
.hero{position:absolute;left:0;top:105px;width:1200px;height:603px;background:linear-gradient(180deg,#8c8a86 0%,#6f6a63 35%,#8a7d6a 62%,#4e4c4a 82%,#6a6760 100%)}
.hero-title{position:absolute;left:91px;display:inline-block;white-space:nowrap;font-family:"Lato",sans-serif;font-weight:700;font-size:30px;letter-spacing:2px;padding:0 22px;height:58px;line-height:58px}
.hero-title.one{top:215px;background:var(--blue);color:var(--white)}
.hero-title.two{top:287px;background:var(--white);color:var(--blue)}
.dots{position:absolute;left:560px;top:554px;display:flex;gap:10px}
.dots i{width:13px;height:13px;border-radius:50%;background:var(--white);display:block}
.dots i:first-child{background:var(--blue)}

/* section headings */
.section-heading{position:absolute;left:0;width:1200px;display:flex;align-items:center;font-family:"Lato",sans-serif;font-weight:700;font-size:27px;letter-spacing:2.5px;color:var(--ink)}
.section-heading .rule{flex:1;height:2px;background:var(--rule)}
.section-heading h2{font:inherit;padding:0 60px;white-space:nowrap}
.section-heading .accent{color:var(--blue)}

.about-text{position:absolute;left:160px;width:880px;top:876px;text-align:center;font-size:16px;line-height:23px;color:var(--text)}
.about-text p+p{margin-top:12px}

/* services */
.services{position:absolute;left:0;top:1061px;width:1200px;height:442px;background:var(--blue)}
.services .notch{position:absolute;left:570px;top:0;width:0;height:0;border-left:29px solid transparent;border-right:29px solid transparent;border-top:27px solid var(--white)}
.services .section-heading{top:75px;color:var(--white)}
.services .section-heading .rule{background:rgba(255,255,255,.7)}
.service-card{position:absolute;top:160px;height:230px;background:var(--card);text-align:center;color:var(--white)}
.service-card.alt{background:var(--card-alt)}
.service-card svg{display:block;margin:34px auto 0}
.service-card h3{margin-top:22px;font-family:"Lato",sans-serif;font-weight:700;font-size:17px;letter-spacing:1.3px}
.service-card p{margin-top:14px;font-size:15px;line-height:23px;color:#d8dadc}

/* split feature */
.feature-photo-left{position:absolute;left:0;top:1503px;width:588px;height:384px;background:linear-gradient(90deg,#1d2024,#2e3236 60%,#3b3f43)}
.feature-photo-right{position:absolute;left:588px;top:1503px;width:612px;height:384px;background:linear-gradient(180deg,#7aa6cf 0%,#a9c3d9 45%,#d8d7d2 62%,#8b8880 82%,#b0a792 100%)}
.feature-item{position:absolute;left:95px;display:flex;align-items:center;gap:18px}
.feature-item .icon{width:72px;height:70px;background:var(--blue);display:flex;align-items:center;justify-content:center}
.feature-item span{font-family:"Lato",sans-serif;font-weight:700;font-size:21px;letter-spacing:1.3px;line-height:26px;color:var(--white);white-space:nowrap}

/* stories */
.avatar{position:absolute;border-radius:50%}
.avatar.sm{width:76px;height:76px;top:2085px}
.avatar.lg{width:206px;height:206px;left:492px;top:2020px;background:linear-gradient(160deg,#d5c8b8,#9a8a7a 60%,#5a5048)}
.arrow{position:absolute;top:2110px;font-size:26px;color:var(--ink);font-family:"Lato",sans-serif;font-weight:700}
.story-name{position:absolute;left:0;width:1190px;top:2259px;text-align:center;font-family:"Dosis",sans-serif;font-weight:600;font-size:25px;color:var(--blue-bright)}
.story-place{position:absolute;left:0;width:1190px;top:2305px;text-align:center;font-family:"Dosis",sans-serif;font-weight:500;font-size:13px;color:#555}

/* map + contacts */
.map{position:absolute;left:0;top:2376px;width:588px;height:424px;background:linear-gradient(160deg,#e4ead9 0%,#eae6dc 45%,#dde5cf 70%,#a9cbe6 100%)}
.map-label{position:absolute;left:0;top:2376px;width:588px;height:30px;background:var(--navy);font-family:"Lato",sans-serif;font-weight:900;font-size:21px;color:var(--white);padding-left:42px;line-height:30px;letter-spacing:1px}
.contacts{position:absolute;left:588px;top:2376px;width:612px;height:424px;background:var(--navy);color:var(--white)}
.contacts h2{position:absolute;left:36px;top:90px;font-family:"Lato",sans-serif;font-weight:700;font-size:26px;letter-spacing:1px}
.contact-line{position:absolute;left:36px;font-family:"Open Sans",sans-serif;font-weight:700;font-size:16px;white-space:nowrap}
.contact-line b{margin-right:16px}
.social{position:absolute;left:40px;top:309px;display:flex;gap:29px}
.social i{display:block;width:14px;height:14px;border-radius:50%;background:var(--white)}
.site-footer{position:absolute;left:0;top:2800px;width:1200px;height:53px;background:var(--footer);color:var(--white);text-align:center;line-height:53px;font-weight:700;font-size:15px;letter-spacing:.6px}
</style>
</head>
<body>

<header class="site-header">
  <div class="brand">RIVOLEX</div>
  <div class="login">
    <svg width="26" height="26" viewBox="0 0 26 26"><circle cx="13" cy="13" r="11.5" fill="none" stroke="#1d5fa3" stroke-width="2"/><circle cx="13" cy="10" r="4" fill="#1d5fa3"/><path d="M6 20c2-4 12-4 14 0" fill="#1d5fa3"/></svg>
    LOGIN
  </div>
  <nav class="nav">
    <span class="active" style="left:592px">HOME</span>
    <span style="left:685px">ABOUT</span>
    <span style="left:784px">TECHNOLOGY</span>
    <span style="left:940px">BLOG</span>
    <span style="left:1023px">CONTACT</span>
  </nav>
</header>

<section class="hero" role="img" aria-label="Silver US semi truck with a branded trailer on a desert highway below rocky mountains">
  <div class="hero-title one">HEAVY LOGISTICS &amp;</div>
  <div class="hero-title two">TRANSPORATION SERVICES</div>
  <div class="dots"><i></i><i></i><i></i><i></i></div>
</section>

<div class="section-heading" style="top:794px">
  <span class="rule"></span><h2><span class="accent">ABOUT OUR</span> COMPANY</h2><span class="rule"></span>
</div>
<div class="about-text">
  <p>Our mission is to provide our clients with safe, consistent and &nbsp;quality transportation solutions. Our logistics team is committed to customer satisfaction, safety and trust. You can be sure your &nbsp;goods will be delivered on time and in the best condition.</p>
  <p>At Harlow Freight customer satisfaction it's our priority.</p>
</div>

<section class="services">
  <span class="notch"></span>
  <div class="section-heading"><span class="rule"></span><h2>OUR SERVICES</h2><span class="rule"></span></div>

  <div class="service-card" style="left:93px;width:251px">
    <svg width="70" height="70" viewBox="0 0 70 70"><circle cx="35" cy="35" r="33" fill="none" stroke="#fff" stroke-width="2"/><rect x="18" y="26" width="22" height="15" fill="#fff"/><path d="M40 30h7l5 6v5H40z" fill="#fff"/><circle cx="25" cy="44" r="3.5" fill="#fff"/><circle cx="46" cy="44" r="3.5" fill="#fff"/></svg>
    <h3>LOGISTICS</h3>
    <p>Our mission is to provide<br>our clients with safe,</p>
  </div>
  <div class="service-card" style="left:352px;width:245px">
    <svg width="70" height="70" viewBox="0 0 70 70"><circle cx="35" cy="35" r="33" fill="none" stroke="#fff" stroke-width="2"/><path d="M20 42a15 15 0 1 1 30 0" fill="none" stroke="#fff" stroke-width="2.5"/><path d="M35 40l6-10" stroke="#fff" stroke-width="2.5"/><circle cx="35" cy="40" r="2.5" fill="#fff"/></svg>
    <h3>DEDICATED</h3>
    <p>Our mission is to provide<br>our clients with safe,</p>
  </div>
  <div class="service-card alt" style="left:605px;width:241px">
    <svg width="70" height="70" viewBox="0 0 70 70"><circle cx="35" cy="35" r="33" fill="none" stroke="#fff" stroke-width="2"/><rect x="22" y="24" width="26" height="16" fill="#fff"/><path d="M16 42h38" stroke="#fff" stroke-width="2.5"/><circle cx="27" cy="45" r="3" fill="#fff"/><circle cx="43" cy="45" r="3" fill="#fff"/></svg>
    <h3>DRY VEN</h3>
    <p>Our mission is to provide<br>our clients with safe,</p>
  </div>
  <div class="service-card" style="left:854px;width:249px">
    <svg width="70" height="70" viewBox="0 0 70 70"><circle cx="35" cy="35" r="33" fill="none" stroke="#fff" stroke-width="2"/><path d="M26 24h8v14H20v-7z" fill="#fff"/><path d="M18 40h34" stroke="#fff" stroke-width="2.5"/><circle cx="25" cy="44" r="3" fill="#fff"/><circle cx="45" cy="44" r="3" fill="#fff"/></svg>
    <h3>EQUIPMENT SALES</h3>
    <p>Our mission is to provide<br>our clients with safe,</p>
  </div>
</section>

<div class="feature-photo-left" role="img" aria-label="Darkened photo of a parked white trailer truck"></div>
<div class="feature-photo-right" role="img" aria-label="Driver in a red shirt walking beside a white US semi truck"></div>

<div class="feature-item" style="top:1569px">
  <div class="icon"><svg width="34" height="34" viewBox="0 0 34 34"><path d="M4 10l13-6 13 6v14l-13 6-13-6z" fill="none" stroke="#fff" stroke-width="2.5"/><path d="M4 10l13 6 13-6M17 16v14" stroke="#fff" stroke-width="2.5" fill="none"/></svg></div>
  <span>TRUCKING<br>SHIPPING SERVICES</span>
</div>
<div class="feature-item" style="top:1657px">
  <div class="icon"><svg width="36" height="30" viewBox="0 0 36 30"><rect x="2" y="6" width="20" height="15" fill="#fff"/><path d="M22 10h7l5 6v5H22z" fill="#fff"/><circle cx="9" cy="24" r="3.5" fill="#fff"/><circle cx="28" cy="24" r="3.5" fill="#fff"/></svg></div>
  <span>SPECIALTY FREIGHT &amp;<br>SHIPPING SERVICES</span>
</div>
<div class="feature-item" style="top:1746px">
  <div class="icon"><svg width="34" height="30" viewBox="0 0 34 30"><path d="M4 4h22v14H12l-6 5v-5H4z" fill="none" stroke="#fff" stroke-width="2.5"/><path d="M28 10h3v12h-2v4l-5-4h-9" fill="none" stroke="#fff" stroke-width="2.5"/></svg></div>
  <span>LOGISTICS<br>MANAGEMENT</span>
</div>

<div class="section-heading" style="top:1924px">
  <span class="rule"></span><h2><span class="accent">OUR SUCCES</span> STORIES</h2><span class="rule"></span>
</div>

<div class="avatar sm" style="left:194px;background:#8a8c8e" role="img" aria-label="Client portrait"></div>
<div class="avatar sm" style="left:287px;background:#9b6e5e" role="img" aria-label="Client portrait"></div>
<div class="avatar sm" style="left:380px;background:#7c6a60" role="img" aria-label="Client portrait"></div>
<span class="arrow" style="left:470px">&lsaquo;</span>
<div class="avatar lg" role="img" aria-label="Featured client portrait"></div>
<span class="arrow" style="left:704px">&rsaquo;</span>
<div class="avatar sm" style="left:738px;background:#6e7c8c" role="img" aria-label="Client portrait"></div>
<div class="avatar sm" style="left:831px;background:#5e5a58" role="img" aria-label="Client portrait"></div>
<div class="avatar sm" style="left:924px;background:#a0685a" role="img" aria-label="Client portrait"></div>

<div class="story-name">Dale Morrow</div>
<div class="story-place">Milton Keynes, United Kingdom</div>

<div class="map" role="img" aria-label="Road map of the United States"></div>
<div class="map-label">MAP</div>

<section class="contacts">
  <h2>CONTACTS</h2>
  <div class="contact-line" style="top:172px"><b>Main Office:</b>1840 Orchard Ln. Dallas, TX 75201</div>
  <div class="contact-line" style="top:207px"><b>Phone Number:</b>1-555-0142-0</div>
  <div class="contact-line" style="top:246px"><b>Email Adress:</b>info@rivolex.com</div>
  <div class="social"><i></i><i></i><i></i><i></i><i></i><i></i></div>
</section>

<footer class="site-footer">© 2017. Rivolex.</footer>

</body>
</html>
```